Web Design job - Condo Debts Collection Business needs a Web Design

I need a site for a client, who works with condo debts collection, and ensure all revenues provided by condo fees will be always available to the building manager of condo on a specific date, regardless of defaults.
I have the visual identity (logo, slogan and colors) of the company, and some requirements on layout (kind of slider, menu options, phone number on a noble position, etc) - maybe I can do a sketch, but I like the idea of give some freedom to designer.

*** PLEASE, we have no interest in templates. We want something new***

Target Market(s)

I have two targets for this design: - Condominium's building manager. This target is looking for a solution to overdue debts on it's condo. - Residents on condominiums. This target wants to live in a better place, where their neighbors pay their condominium fees on time.

Number of Pages Required

1 page

Requirements
Must have
• - Slider with title, some short text related, a nice image (I prefer happy and/or peaceful family, people doing business, happy friends, and so on).
• - I have a special attention to menu. I'm looking for one I can have a nice effect, more elegant, charming, kind of innovative.
• - Phone number on the top (or clearly visible).
• - Member log in area or icon on the top (or clearly visible).
• - News/articles area.
• - Modern fonts, with good quality, sans-serif on areas where reading is more intensive (prefer Google web-fonts).
• - Colors specified on attached files.
Nice to have
• - Clear background color, cause it's better to read larger texts (like articles). Dark backgrounds makes reading difficult.
• - A site with effects (like shadows, lines, curves, gradients, lights) is usually pretty.
• - I pay attention on beautiful footers.
Should not have
• - Images with a lot of money (I don't sell richness, I sell tranquility, peace, harmony, safety).
• - Poor menu.

```html
<!DOCTYPE html>
<html lang="en">
<head>
<meta charset="utf-8">
<title>Norvia – Condominium Debt Solutions</title>
<link href="https://fonts.googleapis.com/css2?family=Raleway:ital,wght@0,400;0,500;0,600;0,700;0,800;1,400&display=swap" rel="stylesheet">
<style>
:root{
  --gold:#e9b92f;
  --gold-deep:#d49a1c;
  --ink:#333333;
  --muted:#666666;
  --topbar:#2a2a2a;
  --soft:#f2f2f2;
  --white:#ffffff;
  --hot:#ee4b3e;
  --new:#f5813a;
}
*{margin:0;padding:0;box-sizing:border-box}
html,body{width:1200px;height:3303px;overflow:hidden}
body{font-family:'Raleway',sans-serif;color:var(--ink);background:var(--white);position:relative}
.abs{position:absolute}

/* top bar */
.topbar{top:0;left:0;width:1200px;height:40px;background:var(--topbar);color:#fff;font-size:12px;font-weight:600}
.topbar .phone{left:150px;top:12px;display:flex;align-items:center;gap:10px}
.topbar .signup{left:922px;top:13px;color:var(--gold)}
.topbar .signin{left:1008px;top:13px}

/* nav */
.nav{top:40px;left:0;width:1200px;height:74px;background:#fff;box-shadow:0 2px 4px rgba(0,0,0,.08);z-index:2}
.brand{left:150px;top:20px;display:flex;align-items:center;gap:8px;font-size:30px;font-weight:800;color:var(--ink);letter-spacing:-.5px}
.brand-mark{width:26px;height:26px;background:var(--gold)}
.menu{left:528px;top:0;height:74px;display:flex;list-style:none;font-size:12px;font-weight:700}
.menu li{height:74px;line-height:78px;padding:0 23px}
.menu li.active{background:#ececec;border-top:3px solid var(--gold);line-height:72px}

/* hero */
.hero{top:114px;left:0;width:1200px;height:524px;background:linear-gradient(100deg,#3d5466 0%,#7a8a98 30%,#c9b7a6 55%,#d8c2ad 75%,#a58f7c 100%)}
.hero-copy{top:170px;left:0;width:1200px;text-align:center;color:#fff}
.hero h1{font-size:34px;font-weight:800;letter-spacing:.5px}
.hero h1 span{color:var(--gold)}
.hero p{font-size:15px;font-weight:600;line-height:21px;width:700px;margin:10px auto 0}
.hero .btns{margin-top:22px;display:flex;justify-content:center;gap:22px}
.btn{width:130px;height:38px;line-height:38px;font-size:12px;font-weight:700;border-radius:3px}
.btn-gold{background:var(--gold);color:var(--ink)}
.btn-line{border:2px solid #fff;line-height:34px}

/* section titles */
.section-title{font-size:18px;font-weight:800;color:var(--gold-deep);letter-spacing:.5px}

/* about */
.about .section-title{left:150px;top:712px}
.about-text{left:150px;top:754px;width:440px;font-size:12.5px;line-height:19.4px;color:var(--ink)}
.about-text p+p{margin-top:18px}
.about-art{left:630px;top:700px}

/* why */
.why{top:1178px;left:0;width:1200px;height:403px;background:var(--soft)}
.why .section-title{top:36px;width:1200px;text-align:center}
.feature{top:118px;width:230px;text-align:center}
.feature svg{display:block;margin:0 auto}
.feature h3{margin-top:24px;font-size:14px;font-weight:700;color:var(--gold-deep)}
.feature p{margin:14px auto 0;width:210px;font-size:12px;line-height:18px;color:var(--ink)}

/* blog */
.blog-title{top:1624px;width:1200px;text-align:center}
.card{width:280px}
.card .thumb{height:170px;position:relative}
.badge{position:absolute;top:-6px;left:0;height:32px;width:66px;color:#fff;font-size:10px;font-weight:800;padding:4px 0 0 8px;line-height:11px;clip-path:polygon(0 0,100% 0,88% 50%,100% 100%,0 100%)}
.badge small{display:block;font-size:6px;font-weight:600;letter-spacing:.3px}
.badge.hot{background:var(--hot)}
.badge.new{background:var(--new)}
.card h4{margin-top:16px;font-size:14px;font-weight:700;color:var(--gold-deep);line-height:18px;text-transform:uppercase}
.card p{margin-top:6px;font-size:12px;line-height:15px;color:var(--muted)}

/* testimonials */
.testi{top:2363px;left:0;width:1200px;height:491px;background:var(--soft)}
.testi .section-title{top:28px;width:1200px;text-align:center}
.testi .sub{top:54px;width:1200px;text-align:center;font-size:17px;font-weight:500;color:var(--ink)}
.quote-card{top:107px;left:225px;width:750px;height:316px;background:#fff;border-radius:6px;box-shadow:0 4px 14px rgba(0,0,0,.18)}
.quote-mark{left:20px;top:10px;font-size:70px;font-weight:800;color:#f0dca2;line-height:1}
.avatar{left:336px;top:20px;width:78px;height:78px;border-radius:50%;background:linear-gradient(#b9c4cc,#8b7a6c)}
.quote-card h5{top:122px;width:750px;text-align:center;font-size:13px;font-weight:600}
.quote-card blockquote{top:148px;left:40px;width:670px;text-align:center;font-size:12px;font-style:italic;line-height:18.5px}
.author{right:54px;top:268px;text-align:center;font-size:11px;line-height:14px}
.author b{display:block;color:var(--gold-deep);font-size:12px;font-weight:700}
.dots{top:458px;left:572px;display:flex;gap:9px}
.dots i{width:6px;height:6px;border-radius:50%;background:#bbb}

/* footer */
.footer{top:2854px;left:0;width:1200px;height:449px;background:linear-gradient(180deg,#4a4d52 0%,#2f3236 60%,#202225 100%);color:#fff}
.footer h6{font-size:13px;font-weight:700;color:var(--gold)}
.footer ul{list-style:none;margin-top:14px;font-size:12px;line-height:26px}
.col-links{left:150px;top:40px}
.col-address{left:310px;top:40px}
.col-address p{margin-top:14px;font-size:12px;line-height:26px}
.col-address h6+p{}
.col-social{left:531px;top:40px}
.col-social li{display:flex;align-items:center;gap:10px;line-height:40px;font-weight:700}
.col-social li i{width:24px;height:24px;border-radius:50%;background:#fff;display:inline-block}
.footer-brand{left:780px;top:140px;display:flex;align-items:center;gap:18px;font-size:84px;font-weight:800;color:#fff;letter-spacing:-1px}
.footer-brand i{width:80px;height:80px;background:var(--gold);display:inline-block}
.subscribe{left:150px;top:288px;width:520px}
.subscribe p{margin-top:10px;font-size:12px;line-height:20px}
.sub-input{margin-top:18px;height:36px;background:#fff;border-radius:3px;display:flex;align-items:center;justify-content:space-between;padding:0 18px;color:#888;font-size:12px}
</style>
</head>
<body>

<div class="abs topbar">
  <div class="abs phone">
    <svg width="16" height="16" viewBox="0 0 24 24"><circle cx="12" cy="12" r="12" fill="#fff"/><path d="M8 6l2 0 1 3-1.5 1a7 7 0 0 0 4.5 4.5l1-1.5 3 1v2a2 2 0 0 1-2 2A11 11 0 0 1 6 8a2 2 0 0 1 2-2z" fill="#2a2a2a"/></svg>
    (+1) 555-204-7731
  </div>
  <div class="abs signup">SIGN UP</div>
  <div class="abs signin">SIGN IN</div>
</div>

<header class="abs nav">
  <div class="abs brand"><span class="brand-mark"></span>norvia</div>
  <ul class="abs menu">
    <li class="active">HOME</li><li>ABOUT US</li><li>PROJECT</li><li>SERVICES</li><li>BLOG</li><li>CONTACT US</li>
  </ul>
</header>

<section class="abs hero" role="img" aria-label="Happy family: a smiling mother and child holding hands">
  <div class="abs hero-copy" style="top:186px">
    <h1><span>THE SOLUTIONS</span> FOR YOUR OVERDUED DEBT</h1>
    <p>Lorem ipsum dolor sit amet, consectetur adipiscing elit. In enim fermentum, vestibulum sem non, lobortis diam. Cras elit lorem, aliquam sed felis sit amet, lacinia posuere ligula.</p>
    <div class="btns"><div class="btn btn-gold">GET STARTED</div><div class="btn btn-line">CONTACT US</div></div>
  </div>
</section>

<section class="about">
  <h2 class="abs section-title">ABOUT US</h2>
  <div class="abs about-text">
    <p>Lorem ipsum dolor sit amet, consectetur adipiscing elit. Mauris vehicula venenatis risus non lobortis. Mauris erat velit, molestie sed lectus non, suscipit semper dui. Vestibulum est lacus, vulputate vitae condimentum ac, ullamcorper et nibh. Praesent lorem ipsum, dictum et nisl ac, rhoncus ultricies odio. Nam eu nulla porta, scelerisque dui tempus, aliquet ligula. Nullam ac enim eget tellus hendrerit maximus. Duis efficitur pharetra urna eget auctor. Nam placerat felis tempus tellus laoreet, sit amet consequat ligula sodales.</p>
    <p>Quisque a tincidunt tellus. Praesent blandit semper mauris sed fermentum. Proin commodo efficitur dui, nec varius elit bibendum sed. Donec venenatis nec magna sed mattis. Donec molestie erat hendrerit tellus suscipit, sed gravida ante mattis. Vestibulum ut consequat ipsum. Cras lacinia mauris sed sem elementum fermentum. Nulla non ex eu metus molestie placerat. Quisque felis velit, vestibulum sagittis efficitur ac, faucibus sit amet tellus. Aenean suscipit erat vitae tortor congue finibus. Vivamus lacinia magna nec ligula rutrum vestibulum.</p>
  </div>
  <svg class="abs about-art" width="520" height="400" viewBox="0 0 520 400">
    <rect x="30" y="110" width="180" height="180" transform="rotate(45 120 200)" fill="none" stroke="#e9b92f" stroke-width="2"/>
    <rect x="290" y="110" width="180" height="180" transform="rotate(45 380 200)" fill="none" stroke="#e9b92f" stroke-width="2"/>
    <g role="img" aria-label="Photo of a smiling, close-knit family group">
      <defs><linearGradient id="fam" x1="0" y1="0" x2="1" y2="1"><stop offset="0" stop-color="#4d6b3a"/><stop offset=".5" stop-color="#a88a70"/><stop offset="1" stop-color="#6a7a52"/></linearGradient></defs>
      <rect x="130" y="68" width="264" height="264" transform="rotate(45 262 200)" fill="url(#fam)"/>
    </g>
  </svg>
</section>

<section class="abs why">
  <h2 class="abs section-title">WHY CHOOSE US</h2>
  <div class="abs feature" style="left:132px">
    <svg width="64" height="64" viewBox="0 0 64 64" fill="none" stroke="#333" stroke-width="2"><rect x="12" y="6" width="40" height="50" fill="#f7e2a1"/><line x1="20" y1="18" x2="44" y2="18"/><line x1="20" y1="26" x2="38" y2="26"/><circle cx="40" cy="42" r="7" fill="#e9b92f"/></svg>
    <h3>PROFESSIONAL</h3><p>Etiam volutpat luctus eros, ut iaculis metus dictum nec. Suspendisse vehicula iaculis ipsum eu laoreet. Vivamus</p>
  </div>
  <div class="abs feature" style="left:369px">
    <svg width="64" height="64" viewBox="0 0 64 64" fill="none" stroke="#333" stroke-width="2"><circle cx="32" cy="34" r="24" fill="#f7e2a1"/><circle cx="32" cy="34" r="18" fill="#fff"/><path d="M32 22v12l8 6"/></svg>
    <h3>FASTEST</h3><p>Etiam volutpat luctus eros, ut iaculis metus dictum nec. Suspendisse vehicula iaculis ipsum eu laoreet. Vivamus</p>
  </div>
  <div class="abs feature" style="left:605px">
    <svg width="64" height="64" viewBox="0 0 64 64" fill="none" stroke="#333" stroke-width="2"><circle cx="32" cy="12" r="7" fill="#e9b92f"/><path d="M28 12l3 3 5-6"/><circle cx="18" cy="34" r="5"/><circle cx="32" cy="34" r="5"/><circle cx="46" cy="34" r="5"/><path d="M10 54v-6a8 8 0 0 1 16 0v6M24 54v-6a8 8 0 0 1 16 0v6M38 54v-6a8 8 0 0 1 16 0v6"/></svg>
    <h3>HIGH EFFICIENCY</h3><p>Etiam volutpat luctus eros, ut iaculis metus dictum nec. Suspendisse vehicula iaculis ipsum eu laoreet. Vivamus</p>
  </div>
  <div class="abs feature" style="left:841px">
    <svg width="64" height="64" viewBox="0 0 64 64" fill="none" stroke="#333" stroke-width="2"><rect x="6" y="8" width="14" height="12" fill="#f7e2a1"/><rect x="44" y="8" width="14" height="12" fill="#e9b92f"/><circle cx="20" cy="32" r="6"/><circle cx="44" cy="32" r="6"/><path d="M8 56v-6a10 10 0 0 1 20 0v6M36 56v-6a10 10 0 0 1 20 0v6"/></svg>
    <h3>TRUST</h3><p>Luctus eros, ut iaculis metus dictum nec. Suspendisse vehicula iaculis ipsum eu laoreet. Vivamus dictum. Cras</p>
  </div>
</section>

<section class="blog">
  <h2 class="abs section-title blog-title">OUR BLOG</h2>
  <article class="abs card" style="left:150px;top:1698px">
    <div class="thumb" role="img" aria-label="Stack of books on a table" style="background:linear-gradient(90deg,#b9c3c2,#d8dcd8 50%,#8a7560)"><span class="badge hot">HOT<small>LIMITED</small></span></div>
    <h4>Lorem ipsum dolor sit amet, consectetur</h4><p>Mauris vehicula venenatis risus non lobortis. Mauris erat velit, molestie sed lectus non.</p>
  </article>
  <article class="abs card" style="left:460px;top:1698px">
    <div class="thumb" role="img" aria-label="Yellow vintage van parked by a wall" style="background:linear-gradient(180deg,#dfe6ea 0%,#e9a42a 55%,#c98515 80%,#8d8a84 100%)"><span class="badge new">NEW<small>LIMITED</small></span></div>
    <h4>Vitae condimentum ac, ullamcorper et nibh</h4><p>Mauris vehicula venenatis risus non lobortis. Mauris erat velit, molestie sed lectus non.</p>
  </article>
  <article class="abs card" style="left:771px;top:1698px">
    <div class="thumb" role="img" aria-label="Smiling child outdoors in warm light" style="background:linear-gradient(120deg,#c9b061,#8e6b3f 50%,#d6b98a)"><span class="badge hot">HOT<small>LIMITED</small></span></div>
    <h4>Nullam ac enim eget tellus hendrerit</h4><p>Proin commodo efficitur dui, nec varius elit bibendum sed. Donec venenatis nec magna</p>
  </article>
  <article class="abs card" style="left:150px;top:2008px">
    <div class="thumb" role="img" aria-label="Sunset over a sandy landscape" style="background:linear-gradient(180deg,#c4b7a6 0%,#f2c57a 35%,#5d5048 50%,#a89682 100%)"><span class="badge new">NEW<small>LIMITED</small></span></div>
    <h4>Lorem ipsum dolor sit amet, consectetur</h4><p>Mauris vehicula venenatis risus non lobortis. Mauris erat velit, molestie sed lectus non.</p>
  </article>
  <article class="abs card" style="left:460px;top:2008px">
    <div class="thumb" role="img" aria-label="Bottle resting among pebbles" style="background:linear-gradient(160deg,#5b6468,#2e3336 50%,#8d8f8c)"><span class="badge hot">HOT<small>LIMITED</small></span></div>
    <h4>Vitae condimentum ac, ullamcorper et nibh</h4><p>Mauris vehicula venenatis risus non lobortis. Mauris erat velit, molestie sed lectus non.</p>
  </article>
  <article class="abs card" style="left:771px;top:2008px">
    <div class="thumb" role="img" aria-label="Stack of books on a table" style="background:linear-gradient(90deg,#b9c3c2,#d8dcd8 50%,#8a7560)"><span class="badge hot">HOT<small>LIMITED</small></span></div>
    <h4>Nullam ac enim eget tellus hendrerit</h4><p>Proin commodo efficitur dui, nec varius elit bibendum sed. Donec venenatis nec magna</p>
  </article>
</section>

<section class="abs testi">
  <h2 class="abs section-title">CLIENT TESTIMONIALS</h2>
  <div class="abs sub">See what our client said</div>
  <div class="abs quote-card">
    <div class="abs quote-mark">&ldquo;</div>
    <div class="abs avatar" role="img" aria-label="Client portrait"></div>
    <h5 class="abs">THE BEST SERVICE I`VE USED SO FAR</h5>
    <blockquote class="abs">Lorem ipsum dolor sit amet, consectetur adipiscing elit. Mauris vehicula venenatis risus non lobortis. Mauris erat velit, molestie sed lectus non, suscipit semper dui. Vestibulum est lacus, vulputate vitae condimentum ac, ullamcorper et nibh. Praesent lorem ipsum, dictum et nisl ac, rhoncus ultricies odio. Nam eu nulla porta, scelerisque dui tempus, aliquet ligula. Nullam ac enim eget tellus hendrerit maximus. Duis efficitur pharetra urna eget auctor. Nam placerat felis tempus tellus laoreet, sit amet consequat ligula sodales.</blockquote>
    <div class="abs author"><b>MR. DANIEL R. HAYES</b>General trial court judge<br>at Westfield Records</div>
  </div>
  <div class="abs dots"><i></i><i></i><i></i><i></i></div>
</section>

<footer class="abs footer" role="img" aria-label="City skyline with office towers, darkened">
  <div class="abs col-links">
    <h6>QUICK LINK</h6>
    <ul><li>HOME</li><li>ABOUT US</li><li>PROJECT</li><li>SERVICES</li><li>CONTACT US</li></ul>
  </div>
  <div class="abs col-address">
    <h6>COMPANY ADDRESS</h6>
    <p>1720 MAPLE CREST DRIVE<br>AUSTIN, TX 78701</p>
    <h6 style="margin-top:18px">CONTACT US</h6>
    <p>555-310-4482<br>555-628-1907</p>
  </div>
  <div class="abs col-social">
    <h6>FOLLOW US</h6>
    <ul><li><i></i>hello@norvia-mail.com</li><li><i></i>hello@norvia-mail.com</li><li><i></i>hello@norvia-mail.com</li></ul>
  </div>
  <div class="abs footer-brand"><i></i>norvia</div>
  <div class="abs subscribe">
    <h6>SUBSCRIBE US NOW:</h6>
    <p>Quisque a tincidunt tellus. Praesent blandit semper mauris sed fermentum. Proin commodo efficitur dui, nec varius elit bibendum sed. Donec venenatis nec magna sed mattis. Donec</p>
    <div class="sub-input"><span>Your Email...</span>
      <svg width="22" height="18" viewBox="0 0 22 18"><path d="M0 0l22 9-22 9 4-9z" fill="#e9b92f"/></svg></div>
  </div>
</footer>

</body>
</html>
```